Stationery Design Project

Minimal Design. Black and White Colours Only.
Need Business Card
With Compliments slip
Letterhead
A4 Folder

Target Market(s)

Luxury architectual designed home owners

Industry/Entity Type

Business

Requirements
Must have
• Black and White colours only. Suggest some good textured stock for business card for future printing. try to use font that is used in my logo our some other minimal modern font.

```html
<!DOCTYPE html>
<html lang="en">
<head>
<meta charset="utf-8">
<title>Kavan Estates — Business Card</title>
<link rel="stylesheet" href="https://fonts.googleapis.com/css2?family=Arimo:wght@400;700&family=Roboto+Condensed:wght@400;700&display=swap">
<style>
  :root {
    --backdrop: #b3b3b3;
    --card-edge: #000000;
    --panel-deep: #1c1c1c;
    --panel-mid: #262626;
    --divider: #555555;
    --ink: #f0f0f0;
    --ink-soft: #dcdcdc;
    --ink-muted: #8e8e8e;
  }
  * { margin: 0; padding: 0; box-sizing: border-box; }
  html, body { width: 992px; height: 1200px; overflow: hidden; }
  body { background: var(--backdrop); position: relative; font-family: "Arimo", Arial, sans-serif; color: var(--ink); }

  .card { position: absolute; left: 22px; width: 946px; border: 2px solid var(--card-edge); overflow: hidden; }

  /* Front */
  .card-front { top: 32px; height: 556px; background: var(--panel-deep); }
  .front-brand { position: absolute; left: 0; right: 0; top: 0; height: 374px; }
  .brand-square { position: absolute; left: 50%; top: 72px; width: 110px; height: 110px; margin-left: -55px; background: var(--ink); }
  .front-name { position: absolute; left: 0; right: 0; top: 258px; text-align: center; font-size: 58px; font-weight: 400; letter-spacing: 1px; color: var(--ink); }
  .front-rule { position: absolute; left: 0; right: 0; top: 374px; height: 4px; background: var(--divider); }
  .front-footer { position: absolute; left: 0; right: 0; top: 378px; bottom: 0; background: var(--panel-mid); }
  .front-url { position: absolute; left: 0; right: 0; top: 86px; text-align: center; font-size: 26px; font-weight: 700; letter-spacing: 14px; color: var(--ink-soft); }

  /* Back */
  .card-back { top: 612px; height: 556px; background: var(--panel-deep); }
  .contact-panel { position: absolute; left: 108px; top: 0; width: 414px; height: 100%; background: var(--panel-mid); }
  .spine { position: absolute; left: 104px; top: 3px; bottom: 0; width: 5px; background: var(--ink); }
  .panel-rule { position: absolute; left: 522px; top: 0; bottom: 0; width: 4px; background: var(--divider); }

  .holder-name { position: absolute; left: 131px; top: 70px; font-family: "Roboto Condensed", "Arial Narrow", sans-serif; font-weight: 700; font-size: 42px; color: var(--ink); }
  .holder-role { position: absolute; left: 131px; top: 126px; font-family: "Roboto Condensed", "Arial Narrow", sans-serif; font-size: 21px; color: var(--ink); }

  .contact-line { position: absolute; left: 131px; font-size: 20px; line-height: 25px; color: var(--ink); }
  .contact-line .label { color: var(--ink-muted); }
  .line-phone { top: 238px; }
  .line-mail { top: 322px; }
  .line-web { top: 372px; }
  .line-address { top: 420px; }

  .icon { position: absolute; }
  .back-brand { position: absolute; left: 526px; right: 0; top: 0; bottom: 0; }
  .back-square { position: absolute; left: 50%; top: 128px; width: 110px; height: 110px; margin-left: -55px; background: var(--ink); }
  .back-name { position: absolute; left: 0; right: 0; top: 300px; text-align: center; font-size: 40px; line-height: 44px; font-weight: 400; color: var(--ink); }
</style>
</head>
<body>

<section class="card card-front">
  <div class="front-brand">
    <div class="brand-square"></div>
    <h1 class="front-name">KAVAN ESTATES</h1>
  </div>
  <div class="front-rule"></div>
  <div class="front-footer">
    <p class="front-url">www.kavanestates.com</p>
  </div>
</section>

<section class="card card-back">
  <div class="contact-panel"></div>
  <div class="spine"></div>
  <div class="panel-rule"></div>

  <!-- profile marker -->
  <svg class="icon" style="left:44px;top:66px" width="64" height="56" viewBox="0 0 64 56" aria-hidden="true">
    <circle cx="28" cy="28" r="26" fill="var(--ink)"/>
    <line x1="54" y1="28" x2="64" y2="28" stroke="var(--ink)" stroke-width="3"/>
  </svg>
  <h2 class="holder-name">MARCUS HALE</h2>
  <p class="holder-role">Managing Director</p>

  <!-- phone -->
  <svg class="icon" style="left:52px;top:240px" width="56" height="44" viewBox="0 0 56 44" aria-hidden="true">
    <circle cx="22" cy="22" r="20" fill="var(--ink)"/>
    <line x1="42" y1="22" x2="56" y2="22" stroke="var(--ink)" stroke-width="3"/>
    <path d="M11 19c0-5 22-5 22 0v3h-6v-3h-10v3h-6z" fill="var(--panel-deep)"/>
    <rect x="14" y="21" width="16" height="10" rx="2" fill="var(--panel-deep)"/>
  </svg>
  <p class="contact-line line-phone">61 400 555 012 <span class="label">Mobile</span><br>61 7 5550 1234 <span class="label">Phone</span></p>

  <!-- mail -->
  <svg class="icon" style="left:52px;top:314px" width="56" height="44" viewBox="0 0 56 44" aria-hidden="true">
    <circle cx="22" cy="22" r="20" fill="var(--ink)"/>
    <line x1="42" y1="22" x2="56" y2="22" stroke="var(--ink)" stroke-width="3"/>
    <rect x="10" y="14" width="24" height="16" fill="none" stroke="var(--panel-deep)" stroke-width="2"/>
    <path d="M10 14l12 9 12-9M10 30l9-8M34 30l-9-8" fill="none" stroke="var(--panel-deep)" stroke-width="2"/>
  </svg>
  <p class="contact-line line-mail">mhale@kavanestates.com</p>

  <!-- web -->
  <svg class="icon" style="left:52px;top:364px" width="56" height="44" viewBox="0 0 56 44" aria-hidden="true">
    <circle cx="22" cy="22" r="20" fill="var(--ink)"/>
    <line x1="42" y1="22" x2="56" y2="22" stroke="var(--ink)" stroke-width="3"/>
    <g fill="none" stroke="var(--panel-deep)" stroke-width="2">
      <circle cx="22" cy="22" r="12"/>
      <ellipse cx="22" cy="22" rx="5" ry="12"/>
      <line x1="10" y1="22" x2="34" y2="22"/>
      <line x1="12" y1="16" x2="32" y2="16"/>
      <line x1="12" y1="28" x2="32" y2="28"/>
    </g>
  </svg>
  <p class="contact-line line-web">www.kavanestates.com</p>

  <!-- address -->
  <svg class="icon" style="left:52px;top:428px" width="56" height="44" viewBox="0 0 56 44" aria-hidden="true">
    <circle cx="22" cy="22" r="20" fill="var(--ink)"/>
    <line x1="42" y1="22" x2="56" y2="22" stroke="var(--ink)" stroke-width="3"/>
    <path d="M22 10l-13 12h4v10h6v-7h6v7h6v-10h4z" fill="var(--panel-deep)"/>
  </svg>
  <p class="contact-line line-address">Level 12, 48 Harbour Rd<br>Brisbane QLD 4000 Australia</p>

  <div class="back-brand">
    <div class="back-square"></div>
    <p class="back-name">KAVAN<br>ESTATES</p>
  </div>
</section>

</body>
</html>
```